Need Business Card for our Real Estate Business with Sales Executive's Picture

PANTONE 484 C ( RED)

PANTONE 2766 C ( BLUE

Industry/Entity Type

Real Estate

Contact Information for Business Card

Name, Mobile, email, & picture of Person
Agency Phone, address, Web address

Requirements
Must have
• Our Logo Colours, Agent Picture,

```html
<!DOCTYPE html>
<html lang="en">
<head>
<meta charset="UTF-8">
<title>Meridian Real Estate – Business Card</title>
<link rel="stylesheet" href="https://fonts.googleapis.com/css2?family=Open+Sans:wght@400&family=Roboto:wght@400;500&display=swap">
<style>
  :root {
    --stage: #414b4c;
    --card-white: #ffffff;
    --navy: #050c5c;
    --ink-navy: #1b2470;
    --maroon: #6b1a1f;
    --photo-light: #eef0ea;
    --photo-mid: #d9dcd3;
  }
  * { margin: 0; padding: 0; box-sizing: border-box; }
  html, body {
    width: 1200px; height: 1092px; overflow: hidden;
    background: var(--stage);
  }
  .stage { position: relative; width: 1200px; height: 1092px; }

  /* Front of card */
  .card-front {
    position: absolute; left: 62px; top: 128px;
    width: 480px; height: 839px;
    background: var(--card-white);
    font-family: "Roboto", Arial, sans-serif;
  }
  .agent-photo {
    position: absolute; left: 0; top: 0; width: 480px; height: 472px;
    background:
      radial-gradient(ellipse 42% 60% at 48% 70%, #2a3f9a 0%, #1d2f86 55%, rgba(29,47,134,0) 100%),
      linear-gradient(180deg, var(--photo-light) 0%, var(--photo-mid) 100%);
  }
  .accent-band {
    position: absolute; left: 0; top: 472px; width: 480px; height: 14px;
    background: linear-gradient(90deg, #1b2470 0%, #3a4490 35%, #f1f1f6 60%, #3a4490 82%, #1b2470 100%);
  }
  .agent-name {
    position: absolute; left: 36px; top: 490px;
    font-size: 37px; font-weight: 400; color: var(--maroon); letter-spacing: 0.5px;
  }
  .agent-title {
    position: absolute; left: 36px; top: 535px;
    font-family: "Open Sans", Arial, sans-serif;
    font-size: 22px; color: var(--ink-navy);
  }
  .office-address {
    position: absolute; left: 36px; top: 578px;
    font-size: 18px; line-height: 25px; color: var(--maroon);
  }
  .contact-list { position: absolute; left: 30px; top: 662px; list-style: none; }
  .contact-item {
    display: flex; align-items: center; height: 36px; margin-bottom: 2px;
    font-size: 19px; color: var(--ink-navy);
  }
  .contact-item svg { width: 30px; height: 30px; margin-right: 25px; flex: none; }

  /* Back of card */
  .card-back {
    position: absolute; left: 679px; top: 114px;
    width: 480px; height: 840px;
    background: var(--navy);
    font-family: "Roboto", Arial, sans-serif;
    color: #ffffff; text-align: center;
  }
  .brand-name {
    position: absolute; left: 0; right: 0; top: 456px;
    font-size: 62px; font-weight: 400; letter-spacing: 4px;
  }
  .brand-tagline {
    position: absolute; left: 0; right: 0; top: 540px;
    font-size: 18px; font-weight: 400; letter-spacing: 3px;
  }
</style>
</head>
<body>
<main class="stage">
  <section class="card-front">
    <div class="agent-photo" role="img" aria-label="Portrait photo of the sales representative in a blue suit against a light wall"></div>
    <div class="accent-band"></div>
    <h1 class="agent-name">DARIUS MERCER</h1>
    <p class="agent-title">Sales Representative</p>
    <p class="office-address">2185 Cedar Ridge Dr<br>#B Lakeview, CA 95432</p>
    <ul class="contact-list">
      <li class="contact-item">
        <svg viewBox="0 0 30 30" aria-hidden="true"><rect x="9" y="3" width="12" height="24" rx="2" fill="none" stroke="#6b1a1f" stroke-width="2.4"/><circle cx="15" cy="23" r="1.3" fill="#6b1a1f"/></svg>
        123 456 789
      </li>
      <li class="contact-item">
        <svg viewBox="0 0 30 30" aria-hidden="true"><path d="M8 5l4 0 2 6-3 2c1.5 3 3.5 5 6 6l2-3 6 2v4c0 1-1 2-2 2C13 24 6 17 6 7c0-1 1-2 2-2z" fill="#6b1a1f"/><path d="M17 5a8 8 0 0 1 8 8M17 9a4 4 0 0 1 4 4" fill="none" stroke="#6b1a1f" stroke-width="2"/></svg>
        123 456 789
      </li>
      <li class="contact-item">
        <svg viewBox="0 0 30 30" aria-hidden="true"><rect x="3" y="7" width="24" height="17" rx="1.5" fill="#6b1a1f"/><path d="M3 8l12 9 12-9" fill="none" stroke="#ffffff" stroke-width="1.8"/></svg>
        hello@meridianhomes.com
      </li>
      <li class="contact-item">
        <svg viewBox="0 0 30 30" aria-hidden="true"><g fill="none" stroke="#6b1a1f" stroke-width="1.8"><circle cx="15" cy="15" r="11"/><ellipse cx="15" cy="15" rx="5" ry="11"/><path d="M4 15h22M6 9h18M6 21h18"/></g></svg>
        meridianhomes.com
      </li>
    </ul>
  </section>

  <section class="card-back">
    <p class="brand-name">MERIDIAN</p>
    <p class="brand-tagline">REAL ESTATE</p>
  </section>
</main>
</body>
</html>
```